New Business Card Design for a Payroll Concierge Company

I need a new business card design that is simple and includes my current information. I am a payroll concierge company that processes payroll for clients who employ household employees and I also manage my client's personal bills, financial records. I want to include my current logo and a logo for an association (PFHKT) I belong too on the front of my business card. I will include both my all my company logo files and the association logo files.

Target Market(s)

People who hire household employees, nannies, home health aides, butlers, maids, etc for wealthy individuals and senior citizens who need help in the home.

Industry/Entity Type

Financial Service

Contact Information for Business Card

Company logo

Name: Martin L. Vellacourt
Managing Director

Office number: 203-555-0148
Business Cell: 203-555-0173

Website: www.tallywagedesk.net
Email: Martin.Vellacourt@tallywagedesk.com

Company address:

17 Heron Lane
Suite 208
Larchmere,ND 06412

Font styles to use
Serif
Sans Serif

Colors
3176b5
85cae6
cee9f5
33a6d7
d3d3d3
dbdbdb

Requirements
Must have
• I need to have my company logo and name, phone numbers, website, email, and address on the card. I also want the association logo on the card somewhere but not too big. Small enough to see the logo maybe on the top or bottom corner. Or some where on there card that it doesn't take away the design.
Nice to have
• i like the blue color in my logo, grey, please see must haves business card details.
Should not have
• PLEASE DO NOT USE THE BUSINESS CARD DESIGNS IN THE FILES I UPLOADED. I AM NOT INTERESTED IN THAT DESIGN. ALSO THE ADDRESS AND WEBSITE ARE INCORRECT ON THOSE DESIGNS. PLEASE USE THE UPDATED INFO ON BUSINESS CARD DETAILS

```html
<!DOCTYPE html>
<html lang="en">
<head>
<meta charset="utf-8">
<title>Tally Wage Desk – Business Card</title>
<link href="https://fonts.googleapis.com/css2?family=Catamaran:wght@400;500;700;800&display=swap" rel="stylesheet">
<style>
  :root {
    --backdrop: #6e6e6e;
    --brand-blue: #0568b0;
    --card-white: #ffffff;
    --ink: #1f2328;
    --badge-blue: #1d5fa6;
  }
  html, body {
    margin: 0;
    padding: 0;
    width: 1200px;
    height: 900px;
    overflow: hidden;
    background: var(--backdrop);
    font-family: "Catamaran", Arial, sans-serif;
  }
  .stage {
    position: relative;
    width: 1200px;
    height: 900px;
  }
  .card {
    position: absolute;
    top: 271px;
    width: 457px;
    height: 281px;
    border-radius: 14px;
    box-shadow: 2px 3px 6px rgba(0,0,0,0.35);
    overflow: hidden;
  }
  .card-front { left: 137px; background: var(--card-white); color: var(--ink); }
  .card-back  { left: 627px; background: var(--brand-blue); }

  .holder-name {
    position: absolute; left: 27px; top: 29px;
    margin: 0; font-size: 14.5px; font-weight: 800;
    color: var(--brand-blue); letter-spacing: 0.3px; line-height: 1;
  }
  .holder-title {
    position: absolute; left: 27px; top: 47px;
    margin: 0; font-size: 13.5px; font-weight: 500; line-height: 1;
  }
  .brand-name {
    position: absolute; margin: 0; font-weight: 800;
    color: var(--brand-blue); letter-spacing: 0.5px; line-height: 1;
    text-transform: uppercase; white-space: nowrap;
  }
  .card-front .brand-name { right: 27px; top: 90px; font-size: 23px; }
  .card-back .brand-name {
    left: 0; right: 0; top: 152px; text-align: center;
    font-size: 33px; color: var(--card-white);
  }

  .contact-list {
    position: absolute; left: 27px; top: 136px;
    margin: 0; padding: 0; list-style: none;
    font-size: 13.5px; font-weight: 500; line-height: 18px;
  }
  .contact-list li { display: flex; align-items: center; gap: 6px; }
  .contact-list svg { width: 11px; height: 11px; fill: var(--brand-blue); flex: none; }

  .address {
    position: absolute; left: 27px; top: 218px;
    margin: 0; font-style: normal; font-size: 13.5px; font-weight: 500; line-height: 17px;
  }
  .membership {
    position: absolute; right: 27px; top: 197px; width: 126px;
    text-align: right;
  }
  .membership-label { margin: 0 37px 2px 0; font-size: 9px; line-height: 1; color: var(--badge-blue); }
  .membership-badge {
    width: 126px; height: 36px; background: var(--badge-blue); border-radius: 2px;
  }
</style>
</head>
<body>
<main class="stage">
  <section class="card card-front" aria-label="Card front">
    <h1 class="holder-name">MARTIN L. VELLACOURT</h1>
    <p class="holder-title">Managing Director</p>
    <p class="brand-name">Tally Wage Desk</p>

    <ul class="contact-list">
      <li>
        <svg viewBox="0 0 12 12" aria-hidden="true"><path d="M1 4c0-2 2-3 5-3s5 1 5 3v1H8.5V3.8h-5V5H1zM2 6h8l1 5H1z"/></svg>
        203-555-0148
      </li>
      <li>
        <svg viewBox="0 0 12 12" aria-hidden="true"><path d="M3 0h6a1 1 0 0 1 1 1v10a1 1 0 0 1-1 1H3a1 1 0 0 1-1-1V1a1 1 0 0 1 1-1zm.5 1.5v8h5v-8zM6 10.2a.6.6 0 1 0 0 1.2.6.6 0 0 0 0-1.2z"/></svg>
        203-555-0173
      </li>
      <li>
        <svg viewBox="0 0 12 12" aria-hidden="true"><path d="M0 2h12v8H0zm1 1v.4l5 3.2 5-3.2V3zm0 1.6V9h10V4.6L6 7.8z"/></svg>
        Martin.Vellacourt@tallywagedesk.com
      </li>
      <li>
        <svg viewBox="0 0 12 12" aria-hidden="true"><path d="M6 0a6 6 0 1 0 0 12A6 6 0 0 0 6 0zm-1 2c1 1 0 2 1 3s2 0 2 2-1 3-1 3a4.5 4.5 0 0 1-5.4-5C3 5 5 3.5 5 2z"/></svg>
        www.tallywagedesk.net
      </li>
    </ul>

    <address class="address">17 Heron Lane<br>Suite 208 Larchmere,ND 06412</address>

    <div class="membership">
      <p class="membership-label">Member of</p>
      <div class="membership-badge" role="img" aria-label="PFHKT association membership badge"></div>
    </div>
  </section>

  <section class="card card-back" aria-label="Card back">
    <p class="brand-name">Tally Wage Desk</p>
  </section>
</main>
</body>
</html>
```